R.T.Pell Logging Web design

Our website needs a redesign. We want it to appear professional and easy to navigate. We will be adding videos and pictures to the new website. We do not sell any products on our website. It should be designed for informational purposes. Our company performs timber harvesting and forest management services. Attached is our new company logo.

www.rtpelllogging-example.com if you want to see our current website.

Industry/Entity Type

Graphic Design

Coding

Coded - Design and coding required

```html
<!DOCTYPE html>
<html lang="en">
<head>
<meta charset="utf-8">
<title>R.T.Pell Logging</title>
<link rel="stylesheet" href="https://fonts.googleapis.com/css2?family=Oswald:wght@300;400;500&family=Cabin+Condensed:wght@400;600;700&family=PT+Serif:ital,wght@0,400;0,700;1,400&display=swap">
<style>
:root{
  --ink:#111111;
  --text:#222222;
  --muted:#8a8a8a;
  --rule:#d6d6d6;
  --gold:#e0a42a;
  --gold-dark:#b47c12;
  --brown:#5b2f1b;
  --brand:#4a2a14;
  --white:#ffffff;
  --black:#000000;
}
*{margin:0;padding:0;box-sizing:border-box}
html,body{width:1200px;height:3125px;overflow:hidden}
body{position:relative;background:var(--white);font-family:"Cabin Condensed",Arial,sans-serif;color:var(--text)}
.abs{position:absolute}

/* header */
.site-header{position:absolute;left:0;top:0;width:1200px;height:94px;background:rgba(255,255,255,.82);z-index:3}
.brand{position:absolute;left:38px;top:22px;display:flex;align-items:center;gap:14px}
.brand-mark{width:44px;height:44px;background:var(--brand)}
.brand-name{font-family:"Cabin Condensed",sans-serif;font-weight:700;font-size:34px;color:var(--brand);letter-spacing:.5px}
.main-nav{position:absolute;right:47px;top:36px;display:flex;gap:30px;font-family:"Oswald",sans-serif;font-size:19px;color:var(--brand);letter-spacing:.5px}

/* hero */
.hero{position:absolute;left:0;top:0;width:1200px;height:853px;
  background:radial-gradient(ellipse 40% 45% at 58% 40%,#f4d486 0%,rgba(226,170,70,.6) 40%,rgba(0,0,0,0) 75%),
  linear-gradient(180deg,#4a3a1e 0%,#7a5a26 35%,#a07a2e 60%,#6a4518 85%,#3c2610 100%)}
.hero-title{position:absolute;left:0;top:286px;width:1200px;text-align:center;font-family:"Oswald",sans-serif;font-weight:300;font-size:54px;color:var(--white);letter-spacing:1px}
.hero-sub{position:absolute;left:400px;top:372px;width:400px;text-align:center;font-size:21px;line-height:28px;color:var(--white)}
.hero-play{position:absolute;left:567px;top:451px}
.hero-cta{position:absolute;left:0;top:556px;width:1200px;text-align:center;color:var(--white);font-size:21px}
.hero-note{position:absolute;left:0;top:586px;width:1200px;text-align:center;color:#f0e2c0;font-size:13px}
.btn{display:block;background:var(--gold);color:var(--ink);font-family:"Oswald",sans-serif;text-align:center}
.hero-btn{position:absolute;left:469px;top:640px;width:265px;height:44px;line-height:44px;font-size:19px;border:2px solid var(--gold-dark)}
.hero-arrow{position:absolute;top:438px;width:44px;height:109px;background:rgba(0,0,0,.55)}
.hero-arrow.left{left:0}.hero-arrow.right{right:0}
.hero-arrow svg{position:absolute;left:12px;top:40px}

/* section labels */
.section-label{position:absolute;left:0;width:1200px;height:30px}
.section-label::before{content:"";position:absolute;left:0;right:0;top:14px;border-top:2px solid var(--rule)}
.section-label span{position:absolute;left:50%;transform:translateX(-50%);top:0;background:var(--white);padding:0 24px;font-family:"Oswald",sans-serif;font-size:21px;letter-spacing:6px;color:var(--ink)}
.section-title{position:absolute;left:0;width:1200px;text-align:center;font-family:"Oswald",sans-serif;font-weight:500;font-size:58px;color:var(--ink);line-height:70px}
.lead{position:absolute;left:147px;width:906px;text-align:center;font-weight:700;font-size:19px;line-height:24px;color:var(--ink)}

/* feature */
.logs{position:absolute;left:44px;top:1213px;width:582px;height:384px;background:radial-gradient(circle at 30% 40%,#d9b58a 0%,#b08552 45%,#6e4a26 100%)}
.feature-box{position:absolute;left:641px;top:1213px;width:512px;height:384px;background:var(--black);color:var(--white);text-align:center}
.feature-kicker{margin-top:111px;font-family:"Oswald",sans-serif;font-weight:300;font-size:24px;letter-spacing:11px}
.feature-title{font-family:"Oswald",sans-serif;font-weight:500;font-size:36px;line-height:44px}
.feature-text{margin:4px auto 0;width:460px;font-weight:700;font-size:18px;line-height:22px}
.feature-btn{position:absolute;left:112px;top:356px;width:285px;height:56px;line-height:56px;font-size:28px;font-weight:500}

/* projects */
.project-circle{position:absolute;border-radius:50%;border:8px solid #d9d4c6}
.project-circle.left{left:15px;top:2025px;width:438px;height:438px;background:radial-gradient(circle at 50% 80%,#9ad05a 0%,#4e8a2a 50%,#1f4a16 100%)}
.project-circle.right{left:775px;top:2025px;width:438px;height:438px;background:radial-gradient(circle at 55% 55%,#d8ec8a 0%,#7fb03a 45%,#3d6b1e 100%)}
.project-circle.center{left:353px;top:2003px;width:482px;height:482px;background:radial-gradient(circle at 50% 50%,#6fae3a 0%,#3f7c22 55%,#244e14 100%);border-color:#cfc9b8}
.project-title{position:absolute;left:353px;top:2190px;width:482px;text-align:center;font-family:"Oswald",sans-serif;font-size:56px;color:var(--white)}
.project-text{position:absolute;left:475px;top:2262px;width:238px;text-align:center;font-size:17px;line-height:19px;color:var(--white)}
.project-btn{position:absolute;left:520px;top:2363px;width:148px;height:38px;line-height:38px;font-size:17px}

/* bottom columns */
.col-left{position:absolute;left:147px;top:2765px;width:540px}
.col-left h3{font-family:"Cabin Condensed",sans-serif;font-weight:600;font-size:33px;color:var(--ink)}
.col-left .intro{margin-top:6px;font-family:"PT Serif",serif;font-style:italic;font-size:17px;line-height:22px;color:var(--ink)}
.col-left .body{margin-top:12px;font-size:16px;line-height:20px;color:#555}
.read-more{margin-top:10px;font-family:"Oswald",sans-serif;font-size:16px;color:var(--brown)}
.col-divider{position:absolute;left:716px;top:2766px;height:266px;border-left:2px solid var(--rule)}
.note{position:absolute;left:753px;width:330px}
.note-head{display:flex;align-items:center;gap:14px;font-family:"PT Serif",serif;font-size:17px;color:var(--ink);text-transform:uppercase}
.note p{margin:10px 0 0 40px;font-size:16px;line-height:19px;color:#666}

/* footer */
.site-footer{position:absolute;left:0;top:3078px;width:1200px;height:47px;background:var(--brown);color:#e7d6c6;font-size:16px;line-height:47px;padding-left:147px;letter-spacing:.5px}
</style>
</head>
<body>

<div class="hero" role="img" aria-label="Sunlit autumn forest with golden light between tall trees"></div>

<header class="site-header">
  <div class="brand"><span class="brand-mark"></span><span class="brand-name">R.T.Pell Logging</span></div>
  <nav class="main-nav"><span>HOME</span><span>ABOUT US</span><span>SERVICES</span><span>LOCTION</span><span>CONTACT US</span></nav>
</header>

<h1 class="hero-title">INCREDIBILE SERVICE</h1>
<p class="hero-sub">Timberline Crew provides everything you need to ensure you have the Luxury you deserve.</p>
<svg class="hero-play" width="66" height="66" viewBox="0 0 66 66"><circle cx="33" cy="33" r="30" fill="none" stroke="#fff" stroke-width="4"/><path d="M26 20 L47 33 L26 46 Z" fill="#fff"/></svg>
<p class="hero-cta">Start your new tour in life today!</p>
<p class="hero-note">No card ever needed</p>
<span class="btn hero-btn">VISIT OUR SHOWROOM!</span>
<span class="hero-arrow left"><svg width="20" height="30" viewBox="0 0 20 30"><path d="M16 3 L4 15 L16 27" fill="none" stroke="#e0a42a" stroke-width="4"/></svg></span>
<span class="hero-arrow right"><svg width="20" height="30" viewBox="0 0 20 30"><path d="M4 3 L16 15 L4 27" fill="none" stroke="#e0a42a" stroke-width="4"/></svg></span>

<div class="section-label" style="top:908px"><span>ABOUT US</span></div>
<h2 class="section-title" style="top:944px">ENSURE THE LUXURY YOU DESERVE</h2>
<p class="lead" style="top:1030px">Receive high-quality professional logging and land clearing services, from R.T.Pell Logging Company based in Pine Hollow, TX. Whether your tract is large or small, our team of experts can provide the resources and solutions you need to get the job done right. Our track record for consistency, timely service, and expertise will continue to keep us competitive in the East Texas timber industry. We pay top dollar for your pine and hardwood timber.</p>

<div class="logs" role="img" aria-label="Stack of cut log ends"></div>
<div class="feature-box">
  <p class="feature-kicker">DELIMBING SERVICES</p>
  <p class="feature-title">AND MECHANICAL FELLING</p>
  <p class="feature-text">Our team of experts can provide the resources and solutions you need to get the job done right. Our track record for consistency, timely service, and expertise will continue to keep us competitive in the East Texas timber industry. We pay top dollar for your pine and hardwood timber.</p>
  <span class="btn feature-btn">START HERE!</span>
</div>

<div class="section-label" style="top:1702px"><span>SERVICES</span></div>
<h2 class="section-title" style="top:1740px">DANGEROUS TREE REMOVAL SERVICES</h2>
<p class="lead" style="top:1826px">Receive high-quality professional logging and land clearing services, from R.T.Pell Logging Company based in Pine Hollow, TX. Whether your tract is large or small, our team of experts can provide the resources and solutions you need to get the job done right. Our track record for consistency, timely service, and expertise will continue to keep us competitive in the East Texas timber industry. We pay top dollar for your pine and hardwood timber.</p>

<div class="project-circle left" role="img" aria-label="Green forest path between trees"></div>
<div class="project-circle right" role="img" aria-label="Tree with bright spring foliage"></div>
<div class="project-circle center" role="img" aria-label="Dense green tree canopy"></div>
<p class="project-title">PROJECT #1</p>
<p class="project-text">Whether your tract is large or small our team of experts can provide the resources and solutions you need to get the job done right.</p>
<span class="btn project-btn">READ MORE</span>

<div class="section-label" style="top:2620px"><span>ABOUT US</span></div>
<h2 class="section-title" style="top:2654px">ENSURE THE LUXURY YOU DESERVE</h2>

<div class="col-left">
  <h3>Good solutionss for your business!</h3>
  <p class="intro">Lorem ipsum dolor sit amet, consectetuer adipiscing elit, sed diam nonummy nibh euismod tincidunt ut laoreet dolore magna aliquam erat volutpat. Ut wisi enim ad minim veniam.</p>
  <p class="body">Lorem ipsum dolor sit amet, consectetuer adipiscing elit, sed diam nonummy nibh euismod tincidunt ut laoreet dolore magna aliquam erat volutpat. Ut wisi enim ad minim veniam, quis nostrud exerci tation ullamcorper suscipit lobortis nisl ut aliquip ex ea commodo consequat. Duis autem vel eum iriure dolor in hendrerit.</p>
  <p class="read-more">READ MORE &raquo;</p>
</div>
<div class="col-divider"></div>
<div class="note" style="top:2776px">
  <div class="note-head"><svg width="26" height="26" viewBox="0 0 26 26"><circle cx="13" cy="13" r="12" fill="#5b2f1b"/><path d="M10 7 L16 13 L10 19" fill="none" stroke="#fff" stroke-width="3"/></svg>Lorem ipsum dolor sit amet</div>
  <p>Ut wisi enim ad minim veniam, quis nostrud exerci tation ullamcorper suscipit lobortis nisl ut.</p>
</div>
<div class="note" style="top:2896px">
  <div class="note-head"><svg width="26" height="26" viewBox="0 0 26 26"><circle cx="13" cy="13" r="12" fill="#5b2f1b"/><path d="M10 7 L16 13 L10 19" fill="none" stroke="#fff" stroke-width="3"/></svg>Lorem ipsum dolor sit amet</div>
  <p>Ut wisi enim ad minim veniam, quis nostrud exerci tation ullamcorper suscipit lobortis nisl ut.</p>
</div>

<footer class="site-footer">&copy; RTPELL 2012-2015. ALL RIGHTS RESERVED</footer>

</body>
</html>
```